BRSP Business Card Design Project

We are a Wedding Film company in Charleston, SC In need of a unique business card. Our website is www.brightspiralreels.example. Check us out to get an idea of who we are and what we do. The design should be upscale but not pretentious. Modern but not cheesy. I will most likely have our cards printed by Zib on the Opal design. I'm also liking the raised designs for our logo. The Wedding Films in our logo on our site is blue so feel free to manipulate our logo for your designs as well.

Industry/Entity Type

Business

Requirements
Must have
• This is the info I want on the card:

Derek Hollisbury
Storyteller

Brightspiral Wedding Reels
www.brightspiralreels.example

555.208.4417
derek@brightspiralreels.example

```html
<!DOCTYPE html>
<html lang="en">
<head>
<meta charset="utf-8">
<title>Brightspiral Wedding Reels – Business Card</title>
<link href="https://fonts.googleapis.com/css2?family=Questrial&family=Great+Vibes&display=swap" rel="stylesheet">
<style>
  :root {
    --backdrop: #e4e4e2;
    --gold-dark: #8a6f3e;
    --gold-mid: #a88c55;
    --gold-light: #c9b27a;
    --card-white: #fbfcfc;
    --card-cool: #dfe6e8;
    --ink: #3a3a3a;
    --white: #ffffff;
  }
  * { box-sizing: border-box; margin: 0; padding: 0; }
  html, body { width: 1200px; height: 880px; overflow: hidden; }
  body {
    background: var(--backdrop);
    font-family: "Questrial", "Helvetica Neue", Arial, sans-serif;
    display: flex;
    align-items: center;
    justify-content: center;
    gap: 40px;
  }
  .card {
    width: 540px;
    height: 309px;
    border-radius: 22px;
    position: relative;
    overflow: hidden;
    box-shadow: 0 10px 28px rgba(0,0,0,0.18);
  }

  /* Front */
  .card--front {
    background: radial-gradient(ellipse at 62% 38%, var(--gold-light) 0%, var(--gold-mid) 45%, var(--gold-dark) 100%);
    display: flex;
    flex-direction: column;
    align-items: center;
    justify-content: center;
    color: var(--white);
  }
  .brand-mark {
    width: 58px; height: 58px;
    border-radius: 50%;
    background: var(--white);
    opacity: 0.9;
    margin-bottom: 16px;
  }
  .brand-name {
    font-size: 50px;
    line-height: 1;
    letter-spacing: 0.5px;
  }
  .brand-tagline {
    font-size: 12px;
    letter-spacing: 6px;
    text-transform: uppercase;
    margin-top: 8px;
  }

  /* Back */
  .card--back {
    background: linear-gradient(200deg, var(--card-white) 0%, var(--card-white) 45%, var(--card-cool) 100%);
    color: var(--ink);
  }
  .back-logo {
    position: absolute;
    left: 30px; top: 32px;
    width: 150px;
    display: flex;
    flex-direction: column;
    align-items: center;
    color: var(--gold-mid);
  }
  .back-logo .brand-mark {
    width: 30px; height: 30px;
    background: var(--gold-mid);
    margin-bottom: 6px;
  }
  .back-logo .brand-name { font-size: 26px; }
  .back-logo .brand-tagline { font-size: 7px; letter-spacing: 3.5px; margin-top: 5px; }

  .name-stripe {
    position: absolute;
    left: 0; right: 0; top: 132px;
    height: 7px;
    background: var(--gold-mid);
  }
  .person {
    position: absolute;
    left: 200px; top: 94px;
    display: flex;
    align-items: baseline;
    gap: 14px;
    white-space: nowrap;
  }
  .person-name {
    font-family: "Great Vibes", cursive;
    font-size: 32px;
    line-height: 36px;
    color: var(--gold-dark);
  }
  .person-role {
    font-size: 13px;
    color: var(--ink);
  }
  .contact {
    position: absolute;
    left: 200px; top: 152px;
    display: grid;
    grid-template-columns: auto auto;
    column-gap: 8px;
    row-gap: 4px;
    font-size: 12px;
    white-space: nowrap;
  }
  .contact dt {
    font-family: "Great Vibes", cursive;
    font-size: 15px;
    color: var(--gold-mid);
    text-align: right;
    line-height: 16px;
  }
  .contact dd { line-height: 16px; }

  .lower-band {
    position: absolute;
    left: 0; right: 0; top: 228px;
    height: 52px;
    background: linear-gradient(90deg, var(--gold-dark), var(--gold-light) 55%, var(--gold-mid));
  }
</style>
</head>
<body>
  <section class="card card--front" aria-label="Card front">
    <div class="brand-mark"></div>
    <div class="brand-name">Brightspiral</div>
    <div class="brand-tagline">Wedding Reels</div>
  </section>

  <section class="card card--back" aria-label="Card back">
    <div class="back-logo">
      <div class="brand-mark"></div>
      <div class="brand-name">Brightspiral</div>
      <div class="brand-tagline">Wedding Reels</div>
    </div>
    <div class="name-stripe"></div>
    <div class="person">
      <span class="person-name">Derek Hollisbury</span>
      <span class="person-role">Storyteller</span>
    </div>
    <dl class="contact">
      <dt>phone :</dt><dd>+ 555.208.4417</dd>
      <dt>email :</dt><dd>derek@brightspiralreels.example</dd>
      <dt>website :</dt><dd>www.brightspiralreels.example</dd>
    </dl>
    <div class="lower-band"></div>
  </section>
</body>
</html>
```